Business Card front and back

I am looking for business card design. I really really like the design file I uploaded named 627788_19250069_3478263_85f427ee_image

Target Market(s)

Corporate Fitness High end Private country club

Industry/Entity Type

Fitness Industry

Contact Information for Business Card

The last image I like as an example I uploaded a bunch of my logos. The file labeled "the signature" is my business card information for you to use

Colors
0054AA
0677BA
7BADD7
CADEEF
E8F1F8

Requirements
Must have
• E-mail sigThe file I uploaded labeled "627788_19250069_3478263_85f427ee_image" with all the plus signs on the back if those could be the logo symbol I uploaded labeled "1 back.png"

```html
<!DOCTYPE html>
<html lang="en">
<head>
<meta charset="utf-8">
<title>Stride Works — Business Card</title>
<link rel="stylesheet" href="https://fonts.googleapis.com/css2?family=Saira:wght@400;500;700&display=swap">
<style>
  :root {
    --stage: #ecedef;
    --card-white: #ffffff;
    --ink: #2b2b2d;
    --card-dark: #2a2a2c;
    --band-dark: #323234;
    --brand-blue: #0677ba;
    --ghost-grey: #e4e4e5;
  }
  * { box-sizing: border-box; margin: 0; padding: 0; }
  html, body {
    width: 1200px; height: 866px; overflow: hidden;
    background: var(--stage);
    font-family: "Saira", sans-serif;
  }
  .sheet {
    width: 1200px; height: 866px;
    display: flex; flex-direction: column; align-items: center; justify-content: center;
    gap: 30px;
  }
  .card {
    position: relative; width: 700px; height: 400px; overflow: hidden;
    box-shadow: 0 8px 24px rgba(0,0,0,.18);
  }

  /* Front */
  .card-front { background: var(--card-white); }
  .front-shapes { position: absolute; inset: 0; }
  .brand {
    position: absolute; left: 44px; top: 78px;
    display: flex; align-items: center; gap: 14px;
  }
  .brand-square { width: 34px; height: 34px; background: var(--brand-blue); flex: none; }
  .brand-name {
    font-weight: 700; font-size: 34px; letter-spacing: 2px;
    color: var(--ink); text-transform: uppercase; line-height: 1; white-space: nowrap;
  }
  .contact-list {
    position: absolute; left: 48px; top: 160px; list-style: none;
  }
  .contact-item {
    display: flex; align-items: center; gap: 12px;
    font-size: 19px; color: var(--ink); height: 32px; white-space: nowrap;
  }
  .contact-icon { width: 18px; height: 18px; fill: var(--brand-blue); flex: none; }
  .portrait-frame {
    position: absolute; left: 446px; top: 36px; width: 204px; height: 204px;
    border: 2px solid var(--brand-blue);
  }
  .portrait {
    position: absolute; left: 454px; top: 44px; width: 188px; height: 188px;
    background: radial-gradient(circle at 55% 40%, #6d6a66 0%, #3a3937 45%, #1d1d1e 100%);
  }
  .person {
    position: absolute; right: 50px; top: 256px; text-align: right;
  }
  .person-name {
    font-weight: 700; font-size: 28px; letter-spacing: 1.5px; line-height: 1.1;
    color: var(--ink); text-transform: uppercase; white-space: nowrap;
  }
  .person-name .surname { color: var(--brand-blue); }
  .person-role { font-size: 20px; color: var(--ink); letter-spacing: 1px; line-height: 1.2; }
  .website {
    position: absolute; right: 50px; top: 352px;
    font-size: 20px; letter-spacing: 1px; color: #ffffff; white-space: nowrap;
  }
  .website .accent { color: var(--brand-blue); }

  /* Back */
  .card-back { background: var(--card-dark); }
  .back-texture {
    position: absolute; inset: 0;
    background:
      radial-gradient(ellipse at 75% 20%, rgba(255,255,255,.16), transparent 55%),
      radial-gradient(ellipse at 20% 85%, rgba(255,255,255,.12), transparent 55%),
      linear-gradient(135deg, #1f1f21 0%, #3a3a3c 50%, #202022 100%);
  }
  .back-brand {
    position: absolute; inset: 0;
    display: flex; align-items: center; justify-content: center; gap: 16px;
  }
  .back-brand .brand-name { color: #ffffff; font-size: 40px; }
  .back-brand .brand-square { width: 40px; height: 40px; }
</style>
</head>
<body>
<main class="sheet">

  <section class="card card-front" aria-label="Business card front">
    <svg class="front-shapes" width="700" height="400" viewBox="0 0 700 400">
      <path d="M0 40 H330 Q420 40 420 130 V300 Q420 340 380 340 H0 Z" fill="var(--ghost-grey)"/>
      <rect x="0" y="392" width="300" height="8" fill="var(--brand-blue)"/>
      <path d="M300 400 Q330 400 340 380 Q352 340 400 340 H700 V400 Z" fill="var(--band-dark)"/>
    </svg>

    <div class="brand">
      <span class="brand-square"></span>
      <span class="brand-name">Stride Works</span>
    </div>

    <ul class="contact-list">
      <li class="contact-item">
        <svg class="contact-icon" viewBox="0 0 24 24"><path d="M6.6 10.8a15 15 0 0 0 6.6 6.6l2.2-2.2c.3-.3.7-.4 1-.2 1.1.4 2.3.6 3.6.6.6 0 1 .4 1 1V20c0 .6-.4 1-1 1A17 17 0 0 1 3 4c0-.6.4-1 1-1h3.5c.6 0 1 .4 1 1 0 1.3.2 2.5.6 3.6.1.3 0 .7-.2 1z"/></svg>
        555-014-2270
      </li>
      <li class="contact-item">
        <svg class="contact-icon" viewBox="0 0 24 24"><path d="M2 5h20v14H2z M2 5l10 8 10-8" fill="var(--brand-blue)" stroke="#ffffff" stroke-width="1.5"/></svg>
        dalen@strideworks.co
      </li>
      <li class="contact-item">
        <svg class="contact-icon" viewBox="0 0 24 24"><path d="M12 2a7 7 0 0 0-7 7c0 5 7 13 7 13s7-8 7-13a7 7 0 0 0-7-7zm0 9.5A2.5 2.5 0 1 1 12 6.5a2.5 2.5 0 0 1 0 5z"/></svg>
        Lakeview Region
      </li>
    </ul>

    <div class="portrait-frame"></div>
    <div class="portrait" role="img" aria-label="Portrait photo of the consultant"></div>

    <div class="person">
      <p class="person-name">Dalen <span class="surname">Marsh</span></p>
      <p class="person-role">Consultant</p>
    </div>

    <p class="website">www.strideworks<span class="accent">.co</span></p>
  </section>

  <section class="card card-back" aria-label="Business card back">
    <div class="back-texture" role="img" aria-label="Dark embossed brand pattern"></div>
    <div class="back-brand">
      <span class="brand-square"></span>
      <span class="brand-name">Stride Works</span>
    </div>
  </section>

</main>
</body>
</html>
```